Silver Creek Plumbing Business card & letter head design

We need a new business card and letter head for our plumbing company called silver creek plumbing. attached is the companys logo. We provide domestic and commercial plumbing services in regional western Australia. We are after Something simple yet nice to look at and something that fits within the trade industry.

Target Market(s)

trade/building industry

Contact Information for Business Card

Darl Hensby
Manager
0461 238 574
enquiries@scplumbwork.net.au
ABN: 47 381 905 462
PCL: 5187

Domestic & Commercial Plumbing
Tip Truck & Excavator hire

Colors

Designer to choose colors to be used in the design.

```html
<!DOCTYPE html>
<html lang="en">
<head>
<meta charset="utf-8">
<title>Silver Creek Plumbing – Letterhead</title>
<link href="https://fonts.googleapis.com/css2?family=Lato:wght@400;700;900&display=swap" rel="stylesheet">
<style>
  :root {
    --backdrop: #cfc3c0;
    --paper: #ffffff;
    --ink: #4a4a4a;
    --brand-blue: #1d5fb3;
    --rule: #6b6b6b;
  }
  html, body {
    margin: 0;
    padding: 0;
    width: 1200px;
    height: 784px;
    overflow: hidden;
    background: var(--backdrop);
  }
  .canvas {
    position: relative;
    width: 1200px;
    height: 784px;
  }
  .letterhead {
    position: absolute;
    left: 338px;
    top: 22px;
    width: 524px;
    height: 740px;
    background: var(--paper);
    box-shadow: 0 2px 10px rgba(0,0,0,0.18);
    font-family: "Lato", sans-serif;
  }
  .letterhead__brand {
    position: absolute;
    top: 56px;
    left: 226px;
    width: 260px;
    margin: 0;
    text-align: center;
    color: var(--brand-blue);
    font-weight: 900;
    font-size: 18px;
    letter-spacing: 0.4px;
    text-transform: uppercase;
    line-height: 1;
    white-space: nowrap;
  }
  .letterhead__rule {
    position: absolute;
    top: 84px;
    left: 48px;
    right: 40px;
    height: 0;
    border-top: 1px solid var(--rule);
  }
  .letterhead__footer {
    position: absolute;
    left: 40px;
    bottom: 34px;
    margin: 0;
    font-size: 11px;
    color: var(--ink);
    letter-spacing: 0.1px;
    white-space: nowrap;
  }
  .letterhead__footer .label {
    color: var(--brand-blue);
  }
  .letterhead__footer .sep {
    margin: 0 5px;
  }
</style>
</head>
<body>
<div class="canvas">
  <section class="letterhead">
    <p class="letterhead__brand">Silver Creek Plumbing</p>
    <div class="letterhead__rule"></div>
    <p class="letterhead__footer">
      0461 238 574<span class="sep">|</span>enquiries@scplumbwork.net.au<span class="sep">|</span><span class="label">ABN:</span> 47 381 905 462<span class="sep">|</span><span class="label">PCL:</span> 5187
    </p>
  </section>
</div>
</body>
</html>
```